Software Platform/Architecture Drawing for website

We need a drawing of a software platform/application.

We are looking for someone to take these abstract concepts and put them into a concrete illustration style. Use the image as baseline description of the framework, not as a template.
See image attached.

The drawing should show the connections between the platform sections, and show that the platform is secure. Platform components can be presented with words or symbols.

There are 2 examples attached to show what kind of graphic we are looking for. Please do not re-create the provided platform drawing in the same concept. We are looking for something more creative to present to our clients.

Thank you.

Healthcare

• the components (not lanes) shown in the KT Platform.pdf design file.
• Please do not follow the same 4-lane concept shown in the attached example. This is an example to show the relationship between the lanes and components. The outside design should not follow the same layout.

```html
<!DOCTYPE html>
<html lang="en">
<head>
<meta charset="utf-8">
<title>KT Platform</title>
<link href="https://fonts.googleapis.com/css2?family=Open+Sans:wght@600;700&display=swap" rel="stylesheet">
<style>
  :root {
    --bg: #13729a;
    --band: #1b3b4b;
    --white: #ffffff;
    --green-dark: #2d7a26;
    --green-tint: #57b847;
    --arrow: #8dc63f;
    --blue: #1a6fa0;
    --blue-tint: #2f8fc7;
    --magenta: #a3195b;
    --magenta-tint: #c0306f;
    --purple: #6a2b8c;
    --purple-tint: #7f3ca3;
    --frame: #e8f3f8;
  }
  * { box-sizing: border-box; margin: 0; padding: 0; }
  html, body { width: 1200px; height: 527px; overflow: hidden; background: var(--bg); }
  body { font-family: "Open Sans", Arial, sans-serif; color: var(--white); }
  .canvas { position: relative; width: 1200px; height: 527px; background: var(--bg); overflow: hidden; }
  .abs { position: absolute; }
  .heading { position: absolute; font-weight: 700; font-size: 15px; text-align: center; line-height: 1.25; white-space: nowrap; }
  .heading--ext { font-size: 16px; padding-bottom: 2px; border-bottom: 1px solid var(--white); }
  .sub { position: absolute; font-size: 11.5px; font-weight: 600; white-space: nowrap; }

  .group { position: absolute; border: 1.5px dashed; border-radius: 3px; padding: 3px; display: flex; flex-direction: column; gap: 4px; }
  .group--green { border-color: #b8e08e; background: var(--green-tint); }
  .group--blue { border-color: #9fd3f0; background: var(--blue-tint); }
  .group--magenta { border-color: #f0a5c7; background: var(--magenta-tint); }
  .group--purple { border-color: #caa3e0; background: var(--purple-tint); }

  .card { position: relative; background: var(--white); border-radius: 2px; display: flex; align-items: center; gap: 5px; padding: 0 6px; font-weight: 700; font-size: 9px; line-height: 1.15; flex: 1; min-height: 0; }
  .card span { flex: 1; text-align: center; }
  .card svg { width: 19px; height: 19px; flex: none; }
  .card--small { font-size: 8.3px; }
  .solo { position: absolute; border: 1.5px dashed; border-radius: 3px; padding: 3px; display: flex; }
  .solo .card { height: 100%; }

  .t-green { color: var(--green-dark); }
  .t-blue { color: var(--blue); }
  .t-magenta { color: var(--magenta); }
  .t-purple { color: var(--purple); }

  .platform-frame { position: absolute; left: 380px; top: 35px; width: 510px; height: 389px; border: 2px solid var(--frame); border-radius: 18px; }
  .secure-label { position: absolute; left: 548px; top: 446px; display: flex; align-items: center; gap: 8px; font-weight: 700; font-size: 18px; }
  .illustration { position: absolute; border-radius: 10px; }
  .band { position: absolute; left: 0; top: 486px; width: 1200px; height: 41px; background: var(--band); }
  .band__title { position: absolute; right: 28px; top: 3px; font-weight: 700; font-size: 26px; letter-spacing: 0.3px; }
  .label { position: absolute; font-weight: 700; font-size: 13.5px; line-height: 1.35; text-align: center; white-space: nowrap; }
</style>
</head>
<body>
<main class="canvas">

  <!-- illustration areas (behind everything) -->
  <div class="illustration" role="img" aria-label="Patient on a green sofa using a tablet, with a TV on a wooden stand" style="left:64px;top:240px;width:232px;height:172px;background:linear-gradient(160deg,#3bb04a 0%,#3aa34a 45%,#6a5a3e 75%,#b98e5a 100%);opacity:.85"></div>
  <div class="illustration" role="img" aria-label="Server rack with glowing status lights" style="left:444px;top:216px;width:108px;height:176px;background:linear-gradient(180deg,#5a8fd8,#2f5fb0);border-radius:6px"></div>
  <div class="illustration" role="img" aria-label="Call center agent with headset at a desk with computer and phone" style="left:628px;top:250px;width:116px;height:126px;background:linear-gradient(160deg,#d8eef6,#3fa6c9 55%,#e07aa8);opacity:.8"></div>
  <div class="illustration" role="img" aria-label="Administrator in purple standing at a large touch screen surrounded by floating charts" style="left:944px;top:208px;width:184px;height:166px;background:linear-gradient(200deg,#d6e8f2,#6fb8dc 50%,#5a2f8a);opacity:.75"></div>

  <!-- connectors and flow arrows -->
  <svg class="abs" width="1200" height="527" style="left:0;top:0" aria-hidden="true">
    <g stroke="#d6ecf5" stroke-width="1" stroke-dasharray="2 3" fill="none">
      <line x1="157" y1="185" x2="152" y2="262"/>
      <line x1="236" y1="212" x2="172" y2="268"/>
      <line x1="300" y1="272" x2="250" y2="310"/>
      <line x1="660" y1="224" x2="655" y2="275"/>
      <line x1="780" y1="320" x2="740" y2="345"/>
      <line x1="749" y1="250" x2="700" y2="285"/>
      <line x1="1095" y1="198" x2="1045" y2="262"/>
    </g>
    <g fill="var(--arrow)">
      <polygon points="340,322 392,322 392,312 424,334 392,356 392,346 340,346"/>
      <polygon points="424,374 372,374 372,364 340,386 372,408 372,398 424,398"/>
      <polygon points="848,363 900,363 900,352 932,375 900,398 900,387 848,387"/>
    </g>
  </svg>

  <!-- patient side -->
  <h2 class="heading" style="left:161px;top:54px;width:170px">Patient Interaction</h2>
  <p class="label" style="left:14px;top:202px;width:92px">Consumer/<br>Patient</p>

  <div class="group group--green" style="left:206px;top:86px;width:94px;height:126px">
    <div class="card t-green">
      <svg viewBox="0 0 20 20" fill="none" stroke="currentColor" stroke-width="1.5"><rect x="3" y="3" width="14" height="14" rx="2"/><line x1="3" y1="7" x2="17" y2="7"/><line x1="6" y1="10.5" x2="14" y2="10.5"/><line x1="6" y1="13.5" x2="12" y2="13.5"/></svg>
      <span>Apps</span>
    </div>
    <div class="card t-green">
      <svg viewBox="0 0 20 20" fill="currentColor"><path d="M2 3h11v7H6l-3 3v-3H2z"/><path d="M8 11h6l3 3v-3h1V6h-3v6H8z" opacity=".8"/></svg>
      <span>SMS</span>
    </div>
    <div class="card t-green">
      <svg viewBox="0 0 20 20" fill="none" stroke="currentColor" stroke-width="1.4"><circle cx="10" cy="10" r="7"/><ellipse cx="10" cy="10" rx="3" ry="7"/><line x1="3" y1="10" x2="17" y2="10"/><line x1="4.5" y1="6" x2="15.5" y2="6"/><line x1="4.5" y1="14" x2="15.5" y2="14"/></svg>
      <span>Web</span>
    </div>
  </div>

  <div class="solo" style="left:99px;top:142px;width:94px;height:43px;border-color:#b8e08e;background:var(--green-tint)">
    <div class="card t-green">
      <svg viewBox="0 0 20 20" fill="none" stroke="currentColor" stroke-width="1.6"><rect x="5" y="5" width="10" height="10" rx="2"/><circle cx="10" cy="10" r="2"/><line x1="7" y1="2" x2="13" y2="2"/><line x1="7" y1="18" x2="13" y2="18"/></svg>
      <span>Wearable Device</span>
    </div>
  </div>

  <div class="solo" style="left:270px;top:230px;width:92px;height:42px;border-color:#b8e08e;background:var(--green-tint)">
    <div class="card t-green">
      <svg viewBox="0 0 20 20" fill="none" stroke="currentColor" stroke-width="1.6"><rect x="2" y="4" width="16" height="10" rx="1"/><line x1="10" y1="14" x2="10" y2="17"/><line x1="6" y1="17" x2="14" y2="17"/></svg>
      <span>Home Device</span>
    </div>
  </div>

  <!-- secure platform -->
  <div class="platform-frame"></div>
  <h2 class="heading" style="left:530px;top:54px;width:92px">Services</h2>
  <div class="group group--blue" style="left:530px;top:80px;width:92px;height:142px">
    <div class="card t-blue" style="flex:0 0 38px">
      <svg viewBox="0 0 20 20" fill="none" stroke="currentColor" stroke-width="1.5"><path d="M7 13a5 5 0 1 1 6 0v2H7z"/><line x1="8" y1="17.5" x2="12" y2="17.5"/><g stroke-width="1.2"><line x1="10" y1="0" x2="10" y2="1.5"/><line x1="2" y1="8" x2="3.5" y2="8"/><line x1="16.5" y1="8" x2="18" y2="8"/></g></svg>
      <span>Logic</span>
    </div>
    <div class="card t-blue" style="flex:0 0 38px">
      <svg viewBox="0 0 20 20" fill="none" stroke="currentColor" stroke-width="1.5"><ellipse cx="10" cy="4.5" rx="6" ry="2.5"/><path d="M4 4.5v11c0 1.4 2.7 2.5 6 2.5s6-1.1 6-2.5v-11"/><path d="M4 8.5c0 1.4 2.7 2.5 6 2.5s6-1.1 6-2.5M4 12.2c0 1.4 2.7 2.5 6 2.5s6-1.1 6-2.5"/></svg>
      <span>DB</span>
    </div>
    <div class="card card--small t-blue">
      <svg viewBox="0 0 20 20" fill="none" stroke="currentColor" stroke-width="1.5"><rect x="1.5" y="1.5" width="17" height="17" rx="1"/><line x1="6" y1="4" x2="6" y2="16"/><line x1="10" y1="4" x2="10" y2="16"/><line x1="14" y1="4" x2="14" y2="16"/><rect x="4.5" y="11" width="3" height="2.5" fill="currentColor"/><rect x="8.5" y="6" width="3" height="2.5" fill="currentColor"/><rect x="12.5" y="9" width="3" height="2.5" fill="currentColor"/></svg>
      <span>Identity<br>&amp; Access<br>Control</span>
    </div>
  </div>

  <h2 class="heading heading--ext" style="left:702px;top:58px;width:104px">External<br>Connections</h2>
  <p class="sub" style="left:713px;top:109px">3rd party APIs:</p>
  <div class="group group--magenta" style="left:749px;top:132px;width:98px;height:132px">
    <div class="card t-magenta">
      <svg viewBox="0 0 20 20"><rect x="2" y="2" width="16" height="16" rx="1" fill="currentColor"/></svg>
      <span>Social Media</span>
    </div>
    <div class="card t-magenta">
      <svg viewBox="0 0 20 20" fill="currentColor"><path d="M2 5h6l2 2h8v10H2z"/><rect x="9" y="9" width="2" height="6" fill="#fff"/><rect x="7" y="11" width="6" height="2" fill="#fff"/></svg>
      <span>EHR</span>
    </div>
    <div class="card t-magenta">
      <svg viewBox="0 0 20 20" fill="none" stroke="currentColor" stroke-width="1.5"><rect x="2" y="5" width="16" height="12"/><path d="M2 5l8 7 8-7"/></svg>
      <span>Email</span>
    </div>
  </div>
  <div class="solo" style="left:640px;top:180px;width:98px;height:44px;border-color:#f0a5c7;background:var(--magenta-tint)">
    <div class="card t-magenta">
      <svg viewBox="0 0 20 20" fill="none" stroke="currentColor" stroke-width="1.6"><path d="M4 11V9a6 6 0 0 1 12 0v2"/><rect x="3" y="10" width="3" height="5" rx="1" fill="currentColor"/><rect x="14" y="10" width="3" height="5" rx="1" fill="currentColor"/><path d="M15.5 15c0 2-2 3-4 3"/></svg>
      <span>Call Center</span>
    </div>
  </div>
  <div class="solo" style="left:770px;top:276px;width:98px;height:44px;border-color:#f0a5c7;background:var(--magenta-tint)">
    <div class="card t-magenta">
      <svg viewBox="0 0 20 20" fill="currentColor" stroke="currentColor" stroke-width="1.3"><line x1="10" y1="10" x2="10" y2="3"/><line x1="10" y1="10" x2="3.5" y2="14"/><line x1="10" y1="10" x2="16.5" y2="14"/><circle cx="10" cy="10" r="3"/><circle cx="10" cy="3" r="2"/><circle cx="3.5" cy="14" r="2"/><circle cx="16.5" cy="14" r="2"/></svg>
      <span>Hub Systems</span>
    </div>
  </div>

  <div class="secure-label">
    <svg width="20" height="24" viewBox="0 0 20 24" aria-hidden="true"><path d="M5 10V7a5 5 0 0 1 10 0v3" fill="none" stroke="#fff" stroke-width="2.4"/><rect x="1" y="10" width="18" height="13" rx="2" fill="#fff"/><rect x="9" y="14" width="2" height="5" fill="var(--bg)"/></svg>
    <span>Secure Platform</span>
  </div>

  <!-- output side -->
  <h2 class="heading" style="left:1055px;top:43px;width:80px">Output</h2>
  <div class="group group--purple" style="left:1048px;top:74px;width:94px;height:124px">
    <div class="card t-purple">
      <svg viewBox="0 0 20 20" fill="none" stroke="currentColor" stroke-width="1.5"><rect x="1.5" y="2.5" width="17" height="12"/><rect x="4" y="5" width="5" height="3" fill="currentColor"/><rect x="11" y="5" width="5" height="7" fill="currentColor"/><line x1="10" y1="14.5" x2="10" y2="17.5"/><line x1="6" y1="17.5" x2="14" y2="17.5"/></svg>
      <span>Web<br>Portal</span>
    </div>
    <div class="card t-purple">
      <svg viewBox="0 0 20 20" fill="none" stroke="currentColor" stroke-width="1.5"><rect x="1.5" y="2.5" width="17" height="12"/><circle cx="12" cy="7" r="1.8" fill="currentColor"/><path d="M9 12.5a3 3 0 0 1 6 0z" fill="currentColor"/><rect x="4" y="5" width="3" height="7" fill="currentColor"/><line x1="10" y1="14.5" x2="10" y2="17.5"/><line x1="6" y1="17.5" x2="14" y2="17.5"/></svg>
      <span>Admin<br>Portal</span>
    </div>
    <div class="card t-purple">
      <svg viewBox="0 0 20 20" fill="none" stroke="currentColor" stroke-width="1.5"><rect x="1.5" y="2.5" width="17" height="12"/><polyline points="4,12 7,8 9,10 12,6"/><circle cx="15" cy="8.5" r="2.2" fill="currentColor"/><line x1="10" y1="14.5" x2="10" y2="17.5"/><line x1="6" y1="17.5" x2="14" y2="17.5"/></svg>
      <span>Client<br>Dashboard</span>
    </div>
  </div>
  <p class="label" style="left:950px;top:377px;width:120px">Administrators</p>

  <footer class="band">
    <p class="band__title">KT PLATFORM</p>
  </footer>
</main>
</body>
</html>
```